Powerpoint template for technical presentation

I need a title page and a template for slides with content. Each content page should have a background and a header for me to add a title to each slide. Each slide needs a slide number.

I would like it to fit in with our existing company and product logo. We develop software used in simulation and GIS environments. Ideally the template will use and complement our existing logos.

TROVE is our product name that we're giving presentations on, Velmora, Inc. is the company name.

Target Market(s)

Professionals in the defense simulation industry.

Industry/Entity Type

Software

Font styles to use
Sans Serif

Requirements
Must have
• Must look good on a projector screen
Nice to have
• Clean and innovative look.

```html
<!DOCTYPE html>
<html lang="en">
<head>
<meta charset="utf-8">
<title>Project Title Here</title>
<link rel="stylesheet" href="https://fonts.googleapis.com/css2?family=Roboto:wght@400;500;700&family=Roboto+Condensed:wght@300;400;700&display=swap">
<style>
  :root {
    --accent: #e8431f;
    --ink: #111111;
    --body-text: #7a7a7a;
    --bg-light: #f7f7f7;
    --bg-mid: #e9e9e9;
    --header-bg: #ffffff;
    --footer-bg: #b5b5b5;
    --footer-ink: #1a1a1a;
    --badge-bg: #666666;
    --white: #ffffff;
  }
  * { margin: 0; padding: 0; box-sizing: border-box; }
  html, body { width: 1200px; height: 900px; overflow: hidden; }
  body { font-family: "Roboto", Arial, sans-serif; background: var(--bg-light); }

  .slide {
    position: relative;
    width: 1200px;
    height: 900px;
    overflow: hidden;
    background:
      radial-gradient(ellipse 520px 420px at 880px 430px, rgba(255,255,255,0.9), rgba(255,255,255,0) 70%),
      radial-gradient(ellipse 700px 600px at 80px 120px, rgba(220,220,220,0.6), rgba(255,255,255,0) 70%),
      linear-gradient(160deg, var(--bg-mid) 0%, var(--bg-light) 45%, var(--bg-mid) 100%);
  }

  .slide-header {
    position: absolute;
    left: 0; top: 0;
    width: 1200px; height: 84px;
    background: linear-gradient(90deg, var(--header-bg) 0%, var(--header-bg) 70%, rgba(255,255,255,0.7) 100%);
    border-bottom: 1px solid #e4e4e4;
  }
  .slide-title {
    position: absolute;
    left: 60px; top: 22px;
    font-family: "Roboto", Arial, sans-serif;
    font-weight: 500;
    font-size: 46px;
    line-height: 1;
    color: var(--ink);
    letter-spacing: 0.3px;
  }
  .slide-title .highlight { color: var(--accent); }

  .product-mark {
    position: absolute;
    right: 24px; top: 22px;
    display: flex;
    align-items: center;
    gap: 12px;
  }
  .product-mark .mark-square {
    width: 22px; height: 22px;
    background: var(--accent);
  }
  .product-mark .mark-name {
    font-family: "Roboto", Arial, sans-serif;
    font-weight: 500;
    font-size: 40px;
    line-height: 1;
    color: var(--ink);
    letter-spacing: 1px;
  }

  .content-list {
    position: absolute;
    left: 60px; top: 160px;
    width: 1000px;
    list-style: none;
  }
  .content-item { position: relative; padding-left: 48px; }
  .content-item + .content-item { margin-top: 58px; }
  .content-item:nth-child(3) { margin-top: 73px; }
  .content-item .bullet {
    position: absolute;
    left: 0; top: 3px;
    width: 30px; height: 30px;
  }
  .item-heading {
    font-family: "Roboto Condensed", "Arial Narrow", sans-serif;
    font-weight: 700;
    font-size: 28px;
    line-height: 36px;
    color: var(--accent);
  }
  .item-body {
    margin-top: 6px;
    margin-left: 3px;
    font-family: "Roboto Condensed", "Arial Narrow", sans-serif;
    font-weight: 300;
    font-size: 21px;
    line-height: 33px;
    color: var(--body-text);
    width: 940px;
  }

  .slide-footer {
    position: absolute;
    left: 0; bottom: 0;
    width: 1200px; height: 78px;
    background: var(--footer-bg);
  }
  .company-mark {
    position: absolute;
    left: 15px; top: 0;
    width: 420px; height: 78px;
    background: var(--white);
    display: flex;
    align-items: center;
    padding-left: 22px;
    gap: 14px;
  }
  .company-mark .mark-name {
    font-family: "Roboto", Arial, sans-serif;
    font-weight: 400;
    font-size: 42px;
    line-height: 1;
    color: #555555;
  }
  .company-mark .mark-square {
    width: 18px; height: 18px;
    background: var(--accent);
  }
  .copyright {
    position: absolute;
    right: 75px; top: 26px;
    font-family: "Roboto", Arial, sans-serif;
    font-size: 22px;
    line-height: 1;
    color: var(--footer-ink);
  }
  .slide-number {
    position: absolute;
    right: 14px; top: 19px;
    width: 42px; height: 38px;
    border: 2px solid var(--white);
    border-radius: 4px;
    background: var(--badge-bg);
    color: var(--white);
    font-family: "Roboto", Arial, sans-serif;
    font-size: 22px;
    line-height: 34px;
    text-align: center;
  }
</style>
</head>
<body>
<main class="slide">
  <header class="slide-header">
    <h1 class="slide-title">Project <span class="highlight">Title Here</span></h1>
    <div class="product-mark">
      <span class="mark-square"></span>
      <span class="mark-name">TROVE</span>
    </div>
  </header>

  <ul class="content-list">
    <li class="content-item">
      <svg class="bullet" viewBox="0 0 30 30" aria-hidden="true">
        <circle cx="15" cy="15" r="15" fill="#e8431f"/>
        <path d="M12 9 L18 15 L12 21" fill="none" stroke="#ffffff" stroke-width="3.5" stroke-linecap="round" stroke-linejoin="round"/>
      </svg>
      <h2 class="item-heading">Lorem ipsum dolor sit ipsum lorem ipsum dolor sit ipsum Lorem ipsu sit ipsum</h2>
      <p class="item-body">Lorem ipsum dolor sit ipsum Lorem ipsum dolor sit ipsum Lorem ipsum dolor&nbsp; Lorem ipsum dolor sit ipsum Lorem ipsum dolor sit ipsum Lorem ipsum dolor Lorem ipsum dolor sit ipsum Lorem ipsum dolor sit ipsum Lorem ipsum dolor&nbsp; Lorem ipsum dolor sit ipsum.</p>
    </li>
    <li class="content-item">
      <svg class="bullet" viewBox="0 0 30 30" aria-hidden="true">
        <circle cx="15" cy="15" r="15" fill="#e8431f"/>
        <path d="M12 9 L18 15 L12 21" fill="none" stroke="#ffffff" stroke-width="3.5" stroke-linecap="round" stroke-linejoin="round"/>
      </svg>
      <h2 class="item-heading">Lorem ipsum dolor sit ipsum lorem ipsum dolor sit ipsum Lorem ipsu sit ipsum</h2>
      <p class="item-body">Lorem ipsum dolor sit ipsum Lorem ipsum dolor sit ipsum Lorem ipsum dolor&nbsp; Lorem ipsum dolor sit ipsum Lorem ipsum dolor sit ipsum Lorem ipsum dolor Lorem ipsum dolor sit ipsum Lorem ipsum dolor sit ipsum Lorem ipsum dolor&nbsp; Lorem ipsum dolor sit ipsum.</p>
    </li>
    <li class="content-item">
      <svg class="bullet" viewBox="0 0 30 30" aria-hidden="true">
        <circle cx="15" cy="15" r="15" fill="#e8431f"/>
        <path d="M12 9 L18 15 L12 21" fill="none" stroke="#ffffff" stroke-width="3.5" stroke-linecap="round" stroke-linejoin="round"/>
      </svg>
      <h2 class="item-heading">Lorem ipsum dolor sit ipsum lorem ipsum dolor sit ipsum Lorem ipsu sit ipsum</h2>
      <p class="item-body">Lorem ipsum dolor sit ipsum Lorem ipsum dolor sit ipsum Lorem ipsum dolor&nbsp; Lorem ipsum dolor sit ipsum Lorem ipsum dolor sit ipsum Lorem ipsum dolor Lorem ipsum dolor sit ipsum Lorem ipsum dolor sit ipsum Lorem ipsum dolor&nbsp; Lorem ipsum dolor sit ipsum.</p>
    </li>
  </ul>

  <footer class="slide-footer">
    <div class="company-mark">
      <span class="mark-name">Velmora, Inc.</span>
      <span class="mark-square"></span>
    </div>
    <p class="copyright">Copyright Text Here</p>
    <div class="slide-number">01</div>
  </footer>
</main>
</body>
</html>
```